Land Buying Company Needs Letterhead for Direct Mail Marketing to Land Owners

We are looking for a professional letterhead that we will be including in our direct mail marketing. We will be sending this to land owners who may be interested in selling or purchasing land.

The letterhead needs to be editable. Headers and footers would look nice, but we are open. We would want it to include our address, website, phone, and email info. For right now the address to use for design purposes would the following:

Address: 415 Bramwell Avenue #600
Dallas, TX 75219
Website - www.quillridgeacres.example
Email - info@quillridgeacres.example
Phone - 866-402-ACRE

I have attached our logo zip file that we just had done on Pixel Guild. Let me know what questions you have, and thank you.

```html
<!DOCTYPE html>
<html lang="en">
<head>
<meta charset="utf-8">
<title>Quillridge Acres Letterhead</title>
<link href="https://fonts.googleapis.com/css2?family=Arimo:wght@400;700&family=Montserrat:wght@400;600&display=swap" rel="stylesheet">
<style>
  :root {
    --forest: #3d5219;
    --leaf: #7cb82f;
    --paper: #f3f3f2;
    --ink: #1b1b1b;
    --stage: #e4e5e4;
    --white: #ffffff;
  }
  * { margin: 0; padding: 0; box-sizing: border-box; }
  html, body { width: 1200px; height: 795px; overflow: hidden; background: var(--stage); }
  .letterhead {
    position: absolute; left: 331px; top: 17px;
    width: 537px; height: 760px;
    background: var(--paper);
    font-family: "Arimo", Arial, sans-serif;
    color: var(--ink);
    overflow: hidden;
    box-shadow: 0 6px 18px rgba(0,0,0,0.12);
  }
  .header-wave { position: absolute; left: 0; top: 0; }
  .brand {
    position: absolute; left: 26px; top: 96px;
    display: flex; align-items: center; gap: 10px;
  }
  .brand-dot { width: 30px; height: 30px; border-radius: 50%; background: var(--white); }
  .brand-name {
    font-family: "Montserrat", Arial, sans-serif; font-weight: 600;
    font-size: 17px; letter-spacing: 1.5px; color: var(--leaf);
  }
  .sender-address {
    position: absolute; right: 30px; top: 18px;
    font-family: "Montserrat", Arial, sans-serif; font-style: normal;
    font-size: 7.5px; line-height: 1.4; color: var(--white); text-align: right;
  }
  .recipient { position: absolute; left: 64px; top: 198px; font-size: 10px; line-height: 1.3; }
  .recipient-name { font-weight: 700; font-size: 11px; }
  .letter {
    position: absolute; left: 106px; top: 262px; width: 380px;
    display: flex; flex-direction: column;
  }
  .letter-body { font-size: 10.5px; line-height: 1.55; }
  .letter-body p + p { margin-top: 16px; }
  .closing { margin-top: 18px; font-size: 10.5px; }
  .signature {
    margin: 6px 0 0 44px; width: 150px; height: 56px;
    background: linear-gradient(90deg, rgba(0,0,0,0.06), rgba(0,0,0,0.02));
    border-radius: 4px;
  }
  .signer { margin: 6px 0 0 90px; font-weight: 700; font-size: 11px; }
  .footer-rule { position: absolute; left: 0; bottom: 30px; width: 100%; height: 3px; background: var(--leaf); }
  .footer-band {
    position: absolute; left: 0; bottom: 0; width: 100%; height: 28px;
    background: var(--forest); color: var(--white);
    font-family: "Montserrat", Arial, sans-serif; font-size: 8px;
    display: flex; align-items: center; padding-left: 30px; gap: 6px;
  }
  .footer-label { color: var(--leaf); font-weight: 600; }
</style>
</head>
<body>
  <main class="letterhead">
    <svg class="header-wave" width="537" height="170" viewBox="0 0 537 170">
      <path d="M0 0 H537 V50 C440 52 370 72 310 112 C250 150 130 148 0 152 Z" fill="var(--forest)"/>
      <path d="M537 50 V62 C450 64 380 88 320 128 C290 148 262 158 240 160 C275 152 292 140 310 112 C370 72 440 52 537 50 Z" fill="var(--leaf)"/>
    </svg>
    <div class="brand">
      <span class="brand-dot"></span>
      <span class="brand-name">QUILLRIDGE ACRES</span>
    </div>
    <address class="sender-address">415 Bramwell Avenue #600,<br>Dallas, TX 75219</address>

    <div class="recipient">
      <div class="recipient-name">JORDAN ELLIS</div>
      <div>Street Name,City Name.</div>
      <div>Zip Coad 0000</div>
    </div>

    <article class="letter">
      <section class="letter-body">
        <p>Lorem Ipsum is simply dummy text of the printing and typesetting industry. Lorem Ipsum has been the industry's standard dummy text ever since the 1500s, when an unknown printer took a galley of type and scrambled it to make a type specimen book. It has survived not only five centuries, but also the leap into electronic typesetting, remaining essentially unchanged. It was popularised in the 1960s with the release of Linotrace sheets containing Lorem Ipsum passages, and more recently with desktop publishing software like Folio PageSetter including versions of Lorem Ipsum.</p>
        <p>It is a long established fact that a reader will be distracted by the readable content of a page when looking at its layout. The point of using Lorem Ipsum is that it has a more-or-less normal distribution of letters, as opposed to using 'Content here, content here', making it look like readable English. Many desktop publishing packages and web page editors now use Lorem Ipsum as their default model text, and a search for 'lorem ipsum' will uncover many web sites still in their infancy. Various versions have evolved over the years, sometimes by accident, sometimes on purpose (injected humour and the like).</p>
      </section>
      <div class="closing">Regards,</div>
      <div class="signature" role="img" aria-label="Handwritten signature of Morgan Hale"></div>
      <div class="signer">Morgan Hale</div>
    </article>

    <div class="footer-rule"></div>
    <footer class="footer-band">
      <span><span class="footer-label">Ph:</span> 866-402-ACRE</span><span>|</span>
      <span><span class="footer-label">Email:</span> info@quillridgeacres.example</span><span>|</span>
      <span><span class="footer-label">Web:</span> www.quillridgeacres.example</span>
    </footer>
  </main>
</body>
</html>
```